Need a New "Register to Download" Graphic

You're the artist! Please get creative and if you think you can make something look better for our front page do so, get our attention and make us pick you!

Currently we have a "Buy Now" button on our website and we want to change this to say "Register to Download" the image must be the same size as the current attached button and be in the form of .png

Do not put any CoinLark or credit card info on the image

On the current image where the CoinLark info is wwritten replace it with "Registration Only Takes 2 Minutes!"

For extra points and to get select you can also change the box graphic on the back and make the "Get Instant Access" look better.

See current graphics http://www.grabtrickly.example
Updates

Project Deadline Extended
Reason: Looking for more submissions

Just made a guarantee on payment, thanks guys! Still waiting for more designs before we choose.

Target Market(s)

Men 18 - 26

Industry/Entity Type

Credit Card

Font styles to use
Sans Serif

Requirements
Must have
• Must blend with website

```html
<!DOCTYPE html>
<html lang="en">
<head>
<meta charset="utf-8">
<title>Register to Download</title>
<link rel="stylesheet" href="https://fonts.googleapis.com/css2?family=Rubik+Dirt&family=Roboto+Condensed:ital,wght@1,700&display=swap">
<style>
  :root {
    --page: #ffffff;
    --red-deep: #5e0305;
    --red-mid: #a8090d;
    --red-bright: #d1141a;
    --white: #ffffff;
    --yellow: #f7f21f;
    --blue: #1d4f93;
    --frame-light: #e6e6e6;
    --frame-dark: #8a8a8a;
    --arrow: #e01b1f;
  }
  html, body { margin: 0; padding: 0; overflow: hidden; background: var(--page); }
  .canvas { position: relative; width: 781px; height: 1200px; overflow: hidden; background: var(--page); }

  .backdrop {
    position: absolute; left: 105px; top: 28px; width: 575px; height: 1142px;
    background: linear-gradient(180deg, var(--red-deep) 0%, var(--red-mid) 22%, var(--red-bright) 50%, var(--red-mid) 78%, var(--red-deep) 100%);
    box-shadow: 0 0 4px rgba(0,0,0,.35);
  }

  .headline {
    position: absolute; left: 105px; top: 175px; width: 610px; margin: 0;
    text-align: center; color: var(--white);
    font-family: "Rubik Dirt", Impact, sans-serif; font-weight: 400;
    font-size: 118px; line-height: 130px; letter-spacing: 2px;
    text-shadow: 4px 5px 4px rgba(0,0,0,.55);
  }
  .headline span { display: block; }

  .arrows { position: absolute; left: 0; top: 0; width: 781px; height: 1200px; }

  .button-frame {
    position: absolute; left: 30px; top: 768px; width: 722px; height: 194px;
    border-radius: 10px;
    background: linear-gradient(180deg, var(--frame-light), var(--frame-dark) 50%, var(--frame-light));
    box-shadow: 0 3px 6px rgba(0,0,0,.4);
  }
  .button-face {
    position: absolute; left: 12px; top: 12px; right: 12px; bottom: 12px;
    background: linear-gradient(180deg, var(--red-deep), var(--red-bright) 50%, var(--red-deep));
    display: flex; align-items: center; justify-content: center;
  }
  .button-label {
    margin: 14px 0 0; font-family: "Rubik Dirt", Impact, sans-serif;
    font-size: 70px; color: var(--white); letter-spacing: 1px;
    text-shadow: 3px 3px 3px rgba(0,0,0,.7);
  }
  .button-label .accent { color: var(--yellow); }

  .tagline {
    position: absolute; left: 200px; top: 740px; margin: 0;
    font-family: "Roboto Condensed", "Arial Narrow", sans-serif;
    font-style: italic; font-weight: 700; font-size: 39px;
    color: var(--blue); -webkit-text-stroke: 6px var(--white); paint-order: stroke fill;
    letter-spacing: -0.5px; white-space: nowrap;
  }
</style>
</head>
<body>
<div class="canvas">
  <div class="backdrop"></div>

  <h1 class="headline"><span>GET</span><span>INSTANT</span><span>ACCESS</span></h1>

  <svg class="arrows" viewBox="0 0 781 1200" aria-hidden="true">
    <g fill="var(--arrow)" stroke="var(--white)" stroke-width="5" stroke-linejoin="round">
      <path d="M30 780 C10 730 60 680 170 680 L178 640 L250 700 L175 760 L172 720 C100 720 70 745 72 780 Z"/>
      <path d="M752 945 C775 1000 720 1045 615 1045 L610 1085 L525 1015 L605 955 L610 1000 C680 1000 715 985 712 945 Z"/>
    </g>
  </svg>

  <div class="button-frame">
    <div class="button-face">
      <p class="button-label">Register to <span class="accent">Download!</span></p>
    </div>
  </div>

  <p class="tagline">Registration Only Takes 2 Minutes!</p>
</div>
</body>
</html>
```